Tarrow Creek plumbing plumbing company business card design

Something sinilar to business card i upload it is my old business card design
And have a good watermark with the logo or majority of the logot in rhe background as watermark

Plumbing business similar to uploaded design with a nice watermark of the logo

Font styles to use
Script

Colors

Designer to choose colors to be used in the design.

```html
<!DOCTYPE html>
<html lang="en">
<head>
<meta charset="utf-8">
<title>Tarrow Creek Plumbing – Business Card</title>
<link href="https://fonts.googleapis.com/css2?family=Lobster&family=Montserrat:wght@400;700&family=Source+Sans+3:wght@300&display=swap" rel="stylesheet">
<style>
  :root {
    --bg: #5a5a5c;
    --white: #ffffff;
    --blue: #037dc2;
    --blue-light: #4da3d8;
    --sky: #b2d9e3;
    --ink: #141414;
    --name-blue: #1f6fa8;
    --mark-faint: rgba(20, 20, 20, 0.05);
  }
  html, body {
    margin: 0;
    width: 1200px;
    height: 1200px;
    overflow: hidden;
    background: var(--bg);
  }
  .sheet { position: relative; width: 1200px; height: 1200px; }
  .card {
    position: absolute;
    left: 170px;
    width: 860px;
    height: 491px;
    overflow: hidden;
    background: var(--white);
    box-shadow: 0 10px 28px rgba(0,0,0,0.35);
  }
  .card--front { top: 80px; }
  .card--back { top: 629px; }
  .card svg.art { position: absolute; inset: 0; }

  .wordmark {
    position: absolute;
    display: flex;
    align-items: center;
    gap: 12px;
    font-family: "Montserrat", sans-serif;
    font-weight: 700;
    color: var(--ink);
    letter-spacing: 0.12em;
    text-transform: uppercase;
    white-space: nowrap;
  }
  .wordmark__dot { flex: none; border-radius: 50%; background: var(--blue); }
  .card--front .wordmark {
    left: 50%; top: 50%;
    transform: translate(-50%, -50%);
    font-size: 34px;
  }
  .card--front .wordmark__dot { width: 30px; height: 30px; }

  .watermark {
    position: absolute;
    font-family: "Montserrat", sans-serif;
    font-weight: 700;
    text-transform: uppercase;
    letter-spacing: 0.1em;
    white-space: nowrap;
    color: var(--mark-faint);
    pointer-events: none;
  }
  .card--front .watermark {
    left: 50%; top: 50%;
    transform: translate(-50%, 20px);
    font-size: 64px;
  }

  .card--back .wordmark { left: 40px; top: 150px; font-size: 17px; }
  .card--back .wordmark__dot { width: 20px; height: 20px; }
  .card--back .watermark { left: 40px; top: 240px; font-size: 40px; }
  .licence {
    position: absolute;
    left: 40px; bottom: 26px;
    font-family: "Source Sans 3", sans-serif;
    font-weight: 300;
    font-size: 18px;
    color: #333;
  }
  .person {
    position: absolute;
    right: 70px; top: 28px;
    text-align: right;
    font-family: "Lobster", cursive;
  }
  .person__name { font-size: 40px; color: var(--name-blue); line-height: 1.1; }
  .person__role { font-size: 26px; color: var(--ink); line-height: 1.1; }
  .contacts {
    position: absolute;
    right: 80px; top: 150px;
    list-style: none;
    margin: 0; padding: 0;
    text-align: right;
    font-family: "Lobster", cursive;
    font-size: 23px;
    color: var(--ink);
  }
  .contacts li { height: 50px; line-height: 50px; white-space: nowrap; }
  .icon-strip {
    position: absolute;
    right: 14px; top: 150px;
    width: 54px; height: 150px;
    background: var(--white);
    display: flex;
    flex-direction: column;
    justify-content: space-around;
    align-items: center;
  }
  .icon-strip svg { width: 24px; height: 24px; }
</style>
</head>
<body>
<main class="sheet">

  <section class="card card--front" aria-label="Card front">
    <svg class="art" viewBox="0 0 860 491" preserveAspectRatio="none" aria-hidden="true">
      <path d="M560 0 L860 0 L860 150 C760 60 660 20 560 0 Z" fill="var(--blue)"/>
      <path d="M560 0 C680 14 790 60 860 140 L860 160 C780 80 680 30 560 0 Z" fill="var(--ink)"/>
      <path d="M0 300 C90 420 260 480 360 491 L0 491 Z" fill="var(--blue)"/>
      <path d="M0 290 C80 400 230 470 360 491 L330 491 C210 470 70 410 0 316 Z" fill="var(--ink)"/>
    </svg>
    <div class="watermark">Tarrow Creek</div>
    <div class="wordmark"><span class="wordmark__dot"></span>Tarrow Creek Plumbing</div>
  </section>

  <section class="card card--back" aria-label="Card back">
    <svg class="art" viewBox="0 0 860 491" preserveAspectRatio="none" aria-hidden="true">
      <path d="M250 0 L860 0 L860 491 L578 491 L578 402 Q578 386 562 381 L448 358 L448 52 Q448 38 436 34 Z" fill="var(--sky)"/>
      <path d="M242 0 L430 36 Q442 40 442 52 L442 362 L560 386 Q572 390 572 402 L572 491"
            fill="none" stroke="var(--blue-light)" stroke-width="12"/>
      <path d="M230 0 L418 36 Q430 40 430 52 L430 372 L548 396 Q560 400 560 412 L560 491"
            fill="none" stroke="var(--blue)" stroke-width="12"/>
    </svg>
    <div class="watermark">Tarrow Creek</div>
    <div class="wordmark"><span class="wordmark__dot"></span>Tarrow Creek Plumbing</div>
    <div class="licence">Lic No. 408731c</div>

    <div class="person">
      <div class="person__name">Declan Marsh</div>
      <div class="person__role">Director</div>
    </div>

    <ul class="contacts">
      <li>0400 555 218</li>
      <li>info@tarrowcreekplumbing.com</li>
      <li>tarrowcreekplumbing.com.au</li>
    </ul>

    <div class="icon-strip">
      <svg viewBox="0 0 24 24" fill="none" stroke="var(--name-blue)" stroke-width="1.4" aria-label="Phone" role="img">
        <path d="M5 3 L9 3 L10 8 L7.5 9.5 C9 13 11 15 14.5 16.5 L16 14 L21 15 L21 19 C21 20 20 21 19 21 C10 21 3 14 3 5 C3 4 4 3 5 3 Z"/>
      </svg>
      <svg viewBox="0 0 24 24" fill="none" stroke="var(--name-blue)" stroke-width="1.4" aria-label="Email" role="img">
        <rect x="2.5" y="5.5" width="19" height="13"/>
        <path d="M2.5 5.5 L12 13 L21.5 5.5 M2.5 18.5 L9.5 11.5 M21.5 18.5 L14.5 11.5"/>
      </svg>
      <svg viewBox="0 0 24 24" fill="none" stroke="var(--name-blue)" stroke-width="1.4" aria-label="Website" role="img">
        <circle cx="12" cy="12" r="9.5"/>
        <ellipse cx="12" cy="12" rx="4.5" ry="9.5"/>
        <path d="M2.5 12 H21.5 M4 7 H20 M4 17 H20"/>
      </svg>
    </div>
  </section>

</main>
</body>
</html>
```